'Gravelmoth Co' Business Cards

Gravelmoth Co is a clothing company geared toward people in the mining industry who are crushing it (literally) We need a design for a business card that has 'GM' similar to the layout of the inspo photo below. Rock textures and maybe some rock dust (see GIF). I Included SVG of our circle logo but not sure how to include without it being boring, would like some ideas. Front should say 'Gravelmoth Co.' (and 'clothing' in smaller letters below) Back should have our webpage 'gravelmothco.ca' our email 'info@gravelmothco.ca' plus a FB and IG icon

```html
<!DOCTYPE html>
<html lang="en">
<head>
<meta charset="utf-8">
<title>Gravelmoth Co. — Business Cards</title>
<link href="https://fonts.googleapis.com/css2?family=Montserrat:wght@300;400;800&display=swap" rel="stylesheet">
<style>
  :root {
    --backdrop: #8a8a8a;
    --rock-light: #a9a496;
    --rock-mid: #8c8373;
    --rock-dark: #5e564a;
    --card-black: #1c1c1c;
    --wordmark-grey: #6f6f6f;
    --contact-tan: #8d8470;
    --icon-ink: #1c1c1c;
    --rule: #5a5548;
    --white: #ffffff;
  }
  html, body {
    margin: 0;
    padding: 0;
    width: 1200px;
    height: 1157px;
    overflow: hidden;
    background: var(--backdrop);
    font-family: "Montserrat", sans-serif;
  }
  .canvas {
    position: relative;
    width: 1200px;
    height: 1157px;
  }
  .card {
    position: absolute;
    left: 250px;
    width: 700px;
    height: 400px;
    box-shadow: 0 14px 28px rgba(0,0,0,0.35);
    overflow: hidden;
  }
  .card--front { top: 120px; }
  .card--back  { top: 620px; background: var(--card-black); }

  .rock-texture {
    position: absolute;
    inset: 0;
    background:
      radial-gradient(ellipse at 70% 25%, var(--rock-light) 0%, transparent 55%),
      radial-gradient(ellipse at 20% 80%, var(--rock-dark) 0%, transparent 50%),
      linear-gradient(160deg, var(--rock-light) 0%, var(--rock-mid) 50%, var(--rock-dark) 100%);
  }
  .front-ring {
    position: absolute;
    left: 60px;
    top: 60px;
    width: 270px;
    height: 270px;
    border-radius: 50%;
    border: 3px solid rgba(255,255,255,0.55);
  }
  .front-brand {
    position: absolute;
    right: 34px;
    top: 172px;
    text-align: center;
    color: var(--white);
    white-space: nowrap;
  }
  .front-brand__name {
    font-weight: 800;
    font-size: 29px;
    letter-spacing: 0.5px;
    line-height: 1;
  }
  .front-brand__tag {
    font-weight: 400;
    font-size: 12px;
    letter-spacing: 9px;
    margin-top: 9px;
    padding-left: 9px;
  }

  .back-brand {
    position: absolute;
    left: 0;
    right: 0;
    top: 112px;
    display: flex;
    align-items: center;
    justify-content: center;
    gap: 16px;
    color: var(--wordmark-grey);
    white-space: nowrap;
  }
  .back-brand__dot {
    width: 46px;
    height: 46px;
    border-radius: 50%;
    background: var(--wordmark-grey);
    flex: none;
  }
  .back-brand__name {
    font-weight: 800;
    font-size: 50px;
    line-height: 1;
  }
  .contact {
    position: absolute;
    left: 0;
    right: 0;
    top: 215px;
    text-align: center;
    color: var(--contact-tan);
    font-weight: 300;
    font-size: 15px;
    letter-spacing: 0.4px;
  }
  .social-row {
    position: absolute;
    left: 120px;
    right: 120px;
    top: 258px;
    height: 28px;
  }
  .social-row svg { display: block; }
  .social-icon__at {
    font-family: "Montserrat", sans-serif;
    font-weight: 800;
    font-size: 15px;
  }
</style>
</head>
<body>
<main class="canvas">
  <section class="card card--front">
    <div class="rock-texture" role="img" aria-label="Grey and tan rock texture background"></div>
    <div class="front-ring"></div>
    <div class="front-brand">
      <div class="front-brand__name">GRAVELMOTH CO.</div>
      <div class="front-brand__tag">CLOTHING</div>
    </div>
  </section>

  <section class="card card--back">
    <div class="back-brand">
      <span class="back-brand__dot"></span>
      <span class="back-brand__name">GRAVELMOTH CO.</span>
    </div>
    <div class="contact">info@gravelmothco.ca | www.gravelmothco.ca</div>
    <div class="social-row">
      <svg width="460" height="28" viewBox="0 0 460 28" role="img" aria-label="Social media links">
        <line x1="0" y1="14" x2="188" y2="14" stroke="var(--rule)" stroke-width="1"/>
        <g class="social-icon social-icon--chat">
          <circle cx="214" cy="14" r="12" fill="var(--contact-tan)"/>
          <path d="M207 9 h14 a2 2 0 0 1 2 2 v6 a2 2 0 0 1 -2 2 h-8 l-4 3 v-3 h-2 a2 2 0 0 1 -2 -2 v-6 a2 2 0 0 1 2 -2 z" fill="var(--icon-ink)"/>
        </g>
        <g class="social-icon social-icon--at">
          <circle cx="246" cy="14" r="12" fill="var(--contact-tan)"/>
          <text class="social-icon__at" x="246" y="19" text-anchor="middle" fill="var(--icon-ink)">@</text>
        </g>
        <line x1="272" y1="14" x2="460" y2="14" stroke="var(--rule)" stroke-width="1"/>
      </svg>
    </div>
  </section>
</main>
</body>
</html>
```